SLA & Internet Advert

Advertise some of our key SLA services & Internet Connectivity services.
Service Level Agreement:
Unlimited Remote, Email, Helpdesk & Telephone Support.
Unlimited Service Calls
Support Hours Monday - Saturday 7am-10pm Sunday till 5pm
Free additional visits during quorlam periods
Free remote access to school server for staff members
Free mobile device management for tablet devices
Free Email&Webhosting Service
Remote support on every device in school allowing us to close 90% of tickets within 30 mins.
Service Level Agreement Package 1 - Includes all the above + 1 Site visit every 2 weeks £2,500 per annum
Service Level Agreement Package 2 - Includes all the above + 1 Site Visit every week £4,500 per annum
Service Level Agreement Package 3 - Includes all the above + 2 Site visits every week - £7,540 per annum
Internet Connectivity (medium/large Primary)
Managed Firewall
Managed Web filter & Safeguarding
User reporting portal/email reporting.
Main Internet Line 1000 mb/s download 100mb/s upload
Back up Internet Line 80mb/s download 20mb/s upload
100% uptime guaranteed.
£3000 per annum
Internet Connectivity (Small Primary School)
Managed Firewall
£2100 per annum
My website is https://www.varnoquell.co.uk if you need any further information like phone numbers / email address etc
Education

```html
<!DOCTYPE html>
<html lang="en">
<head>
<meta charset="utf-8">
<title>Varnoquell – SLA & Internet Connectivity</title>
<link href="https://fonts.googleapis.com/css2?family=Poppins:wght@400;500;600;700;800&family=Syncopate:wght@400;700&family=Michroma&display=swap" rel="stylesheet">
<style>
  :root{
    --blue:#0b6fc4;
    --blue-dark:#0a4f9a;
    --orange:#f47a3c;
    --ink:#222;
    --charcoal:#2b2b2b;
    --line:#c9c9c9;
    --paper:#fff;
  }
  *{box-sizing:border-box;margin:0;padding:0}
  html,body{width:783px;height:1200px;overflow:hidden;background:var(--paper)}
  body{font-family:"Poppins",sans-serif;color:var(--ink);position:relative}
  .abs{position:absolute}

  /* brand */
  .brand{left:46px;top:58px;display:flex;align-items:center;gap:10px}
  .brand-square{width:26px;height:26px;background:var(--blue);border-radius:4px}
  .brand-name{font-weight:800;font-size:30px;color:var(--blue);letter-spacing:1px}

  /* hero */
  .hero{left:0;top:143px;width:397px;height:265px;background:linear-gradient(135deg,var(--blue) 0%,var(--blue-dark) 100%);padding:28px 0 0 46px;color:#fff}
  .hero h1{font-family:"Syncopate","Michroma",sans-serif;font-weight:700;line-height:1.02;white-space:nowrap}
  .hero .k1{display:block;font-weight:400;font-size:24px}
  .hero .k2{display:block;font-size:22px}
  .hero .k3{display:block;font-size:36px;color:var(--orange)}
  .hero .k4{display:block;font-size:24px}
  .hero-rule{margin:12px 0 10px;width:312px;height:1px;background:rgba(255,255,255,.6);position:relative}
  .hero-rule::before{content:"";position:absolute;left:0;top:-2px;width:52px;height:5px;border-radius:3px;background:#fff}
  .hero p{font-size:15px;font-weight:600;line-height:1.25;width:320px}

  .photo-frame{left:400px;top:30px;width:360px;height:365px}
  .photo{left:409px;top:35px;width:330px;height:355px;border-radius:0 0 56px 70px;background:linear-gradient(160deg,#dfe7ef 0%,#9aa7b3 55%,#4b5663 100%)}

  /* SLA */
  .sla{left:47px;top:452px;width:690px;height:344px;border:1.5px solid var(--line);border-radius:8px}
  .sec-title{position:absolute;top:-13px;left:50%;transform:translateX(-50%);background:#fff;padding:0 6px;font-weight:700;font-size:17px;white-space:nowrap}
  .sec-title span{color:var(--blue)}
  .sla-cols{position:absolute;left:34px;top:24px;right:30px;display:flex;gap:34px}
  .sla-cols ul{list-style:none;flex:1}
  .sla-cols li{position:relative;padding-left:18px;font-size:13px;font-weight:600;line-height:1.12;margin-bottom:15px}
  .sla-cols li::before{content:"";position:absolute;left:0;top:4px;width:8px;height:8px;border-radius:50%;border:2.5px solid var(--orange);box-sizing:border-box}
  .sla-note{font-size:11px;font-weight:600;line-height:1.2}
  .sla-note .big{display:block;font-size:13.5px;font-weight:500}
  .sla-note em{font-style:normal;color:var(--orange);font-weight:600}

  .pkg{top:658px;width:205px;height:182px;border-radius:10px;overflow:hidden;color:#fff;text-align:center}
  .pkg-head{background:var(--charcoal);height:68px;padding-top:12px;border-radius:10px 10px 0 0;position:relative}
  .pkg-head::after{content:"";position:absolute;left:50%;bottom:-14px;transform:translateX(-50%);width:120px;height:28px;background:var(--charcoal);border-radius:0 0 60px 60px}
  .pkg-head b{display:block;font-size:13.5px;font-weight:600}
  .pkg-head i{position:relative;z-index:1;display:block;font-style:normal;font-size:12.5px;font-weight:600;margin-top:4px}
  .pkg-body{height:114px;padding-top:24px;font-size:13px;font-weight:600;line-height:1.2}
  .pkg-price{position:absolute;left:50%;bottom:0;transform:translateX(-50%);background:#e9e9e9;color:var(--ink);border-radius:16px 16px 0 0;padding:4px 14px 3px;font-weight:700;font-size:17px;white-space:nowrap}
  .pkg-price small{font-size:9px;font-weight:400}
  .pkg-price sup{font-size:10px}
  .pkg.blue .pkg-body{background:var(--blue)} .pkg.blue i{color:var(--orange)}
  .pkg.orange .pkg-body{background:var(--orange)} .pkg.orange i{color:#2a8ee0}

  /* internet */
  .net{top:870px;height:204px;border:1.5px solid var(--line);border-radius:8px}
  .net h2{position:absolute;top:-12px;left:10px;background:#fff;padding:0 6px;font-size:17px;font-weight:700;white-space:nowrap}
  .net h2 span{color:var(--blue)}
  .net .sub{position:absolute;top:12px;left:16px;font-size:11.5px;font-weight:600}
  .net ul{list-style:none}
  .net li{position:relative;padding-left:15px;font-size:11px;line-height:1.1;margin-bottom:12px;white-space:nowrap}
  .net li::before{content:"";position:absolute;left:0;top:3px;width:7px;height:7px;border-radius:50%;border:2.5px solid var(--orange);box-sizing:border-box}
  .net li b{font-weight:700}
  .net-price{position:absolute;bottom:-14px;left:18px;background:var(--charcoal);color:#fff;border-radius:0 12px 12px 0;padding:2px 14px 2px 10px;font-size:22px;font-weight:700;white-space:nowrap}
  .net-price sup{font-size:11px}
  .net-price small{font-size:14px;font-weight:500}

  /* footer */
  .footer{left:0;top:1102px;width:783px;height:98px;background:var(--charcoal);color:#fff}
  .footer-blue{left:0;top:0;height:98px;width:270px}
  .phone{left:44px;top:36px;display:flex;align-items:center;gap:10px;font-weight:700;font-size:21px}
  .addr{left:288px;top:34px;display:flex;gap:8px;font-size:13px;font-weight:600;line-height:1.2}
  .web{left:572px;top:34px;display:flex;gap:8px;font-size:13px;font-weight:600}
</style>
</head>
<body>

<div class="abs brand"><div class="brand-square"></div><div class="brand-name">VARNOQUELL</div></div>

<svg class="abs photo-frame" viewBox="0 0 360 365" aria-hidden="true">
  <path d="M349 5 V290 Q349 358 284 358 H76 Q14 358 8 306" fill="none" stroke="var(--orange)" stroke-width="8"/>
</svg>
<div class="abs photo" role="img" aria-label="Photo of three young colleagues gathered around a laptop with a wifi symbol above them"></div>

<section class="abs hero">
  <h1><span class="k1">OUR KEY</span><span class="k2">SLA SERVICES &amp;</span><span class="k3">INTERNET</span><span class="k4">CONNECTIVITY</span></h1>
  <div class="hero-rule"></div>
  <p>We offer fast, flexible, reliable and cost effective ICT support for Education</p>
</section>

<section class="abs sla">
  <div class="sec-title">SERVICE LEVEL <span>AGREEMENT*</span></div>
  <div class="sla-cols">
    <ul>
      <li>Unlimited Remote, Email, Helpdesk &amp;<br>Telephone Support.</li>
      <li>Unlimited Service Calls</li>
      <li>Free additional visits during quorlam<br>periods</li>
      <li>Support Hours Monday - Saturday<br>7am-10pm Sunday till 5pm</li>
    </ul>
    <ul>
      <li>Free remote access to school server for<br>staff members</li>
      <li>Free mobile device management for<br>tablet devices</li>
      <li>Free Email &amp; Webhosting Service</li>
      <div class="sla-note">Remote support on every device in school<br>allowing us to close<span class="big"><em>90% of</em> tickets within <em>30 mins.</em></span></div>
    </ul>
  </div>
</section>

<div class="abs pkg blue" style="left:64px">
  <div class="pkg-head"><b>Service Level Agreement</b><i>PACKAGE 1</i></div>
  <div class="pkg-body">Includes all the above*<br>+ 1 Site visit<br>every 2 weeks</div>
  <div class="pkg-price"><sup>£</sup>2,500 <small>per annum</small></div>
</div>
<div class="abs pkg orange" style="left:289px">
  <div class="pkg-head"><b>Service Level Agreement</b><i>PACKAGE 2</i></div>
  <div class="pkg-body">Includes all the above*<br>+ 1 Site visit<br>every weeks</div>
  <div class="pkg-price"><sup>£</sup>4,500 <small>per annum</small></div>
</div>
<div class="abs pkg blue" style="left:514px">
  <div class="pkg-head"><b>Service Level Agreement</b><i>PACKAGE 3</i></div>
  <div class="pkg-body">Includes all the above*<br>+ 2 Site visit<br>every weeks</div>
  <div class="pkg-price"><sup>£</sup>7,540 <small>per annum</small></div>
</div>

<section class="abs net" style="left:47px;width:316px">
  <h2>INTERNET <span>CONNECTIVITY</span></h2>
  <div class="sub">(Medium/large Primary)</div>
  <div style="position:absolute;left:16px;top:38px;display:flex;gap:10px">
    <ul style="width:145px">
      <li>Managed Firewall</li>
      <li>Managed Web filter &amp;<br>Safeguarding</li>
      <li>User reporting portal/<br>email reporting.</li>
      <li>Main Internet Line<br><b>1000 mb/s</b> download</li>
    </ul>
    <ul style="width:140px">
      <li><b>100mb/s</b> upload</li>
      <li>Back up Internet Line</li>
      <li><b>80mb/s</b> download<br><b>20mb/s</b> upload</li>
      <li>100% uptime<br>guaranteed.</li>
    </ul>
  </div>
  <div class="net-price"><sup>£</sup>3000 <small>per annum</small></div>
</section>

<section class="abs net" style="left:407px;width:330px">
  <h2>INTERNET <span>CONNECTIVITY</span></h2>
  <div class="sub">(Small Primary School)</div>
  <ul style="position:absolute;left:16px;top:40px;width:300px">
    <li style="margin-bottom:17px">Managed Firewall</li>
    <li style="margin-bottom:17px">Managed Web filter &amp; Safeguarding</li>
    <li style="margin-bottom:17px">User reporting portal/email reporting.</li>
    <li>Main Internet Line <b>1000 mb/s</b> download<br><b>100mb/s</b> upload</li>
  </ul>
  <div class="net-price"><sup>£</sup>2100 <small>per annum</small></div>
</section>

<footer class="abs footer">
  <svg class="abs footer-blue" viewBox="0 0 270 98" preserveAspectRatio="none" aria-hidden="true"><polygon points="0,0 240,0 270,98 0,98" fill="var(--blue)"/></svg>
  <div class="abs phone">
    <svg width="16" height="16" viewBox="0 0 24 24" aria-hidden="true"><path d="M6.6 10.8a15 15 0 0 0 6.6 6.6l2.2-2.2c.3-.3.7-.4 1-.2 1.1.4 2.3.6 3.6.6.6 0 1 .4 1 1V20c0 .6-.4 1-1 1A17 17 0 0 1 3 4c0-.6.4-1 1-1h3.5c.6 0 1 .4 1 1 0 1.3.2 2.5.6 3.6.1.3 0 .7-.2 1z" fill="var(--orange)"/></svg>
    +44 161 555 0147
  </div>
  <div class="abs addr">
    <svg width="14" height="18" viewBox="0 0 24 30" aria-hidden="true"><path d="M12 0a10 10 0 0 0-10 10c0 7.5 10 20 10 20s10-12.5 10-20A10 10 0 0 0 12 0zm0 14a4 4 0 1 1 0-8 4 4 0 0 1 0 8z" fill="var(--orange)"/></svg>
    <span>Halden House, Corrow Street, Bury<br>United Kingdom</span>
  </div>
  <div class="abs web">
    <svg width="14" height="14" viewBox="0 0 24 24" aria-hidden="true"><g fill="none" stroke="var(--orange)" stroke-width="2"><circle cx="12" cy="12" r="10"/><path d="M2 12h20M12 2c3 3 3 17 0 20M12 2c-3 3-3 17 0 20"/></g></svg>
    <span>www.varnoquell.co.uk</span>
  </div>
</footer>

</body>
</html>
```